Modern Real Estate Sign For Realtor

We need to real estate sign 24x36 or (24x30 if it fits better) Sign that will be attached to a post at homes that are for sale. I like the style of the Meridian 40 yard signs I attached and PD sign with the white trim around it. I Also attached my business card with my logo and name. I would like a black sign with white writing.  I would also like to see options with my headshot included on the sign, either centered or on the right side. The following text should go on the sign:
Logo at the top.
Marcus Hollet
555.317.2096
Marcus@MHolletHomes.example

Requirements
Must have
- Logo at the top.
- Marcus Hollet
- 555.317.2096
- Marcus@MHolletHomes.example

Nice to have
- Headshot open to different design options for how it will be placed on the sign.
- MHolletHomes.example

```html
<!DOCTYPE html>
<html lang="en">
<head>
<meta charset="utf-8">
<title>Hollet Homes Yard Sign</title>
<link rel="stylesheet" href="https://fonts.googleapis.com/css2?family=Raleway:wght@300;500&display=swap">
<style>
  :root {
    --page: #ffffff;
    --sign-black: #000000;
    --ink-white: #ffffff;
    --trim-tan: #bfb28e;
    --photo-green: #6f8a4e;
    --photo-grey: #9a9590;
  }
  * { margin: 0; padding: 0; box-sizing: border-box; }
  html, body {
    width: 1200px;
    height: 999px;
    overflow: hidden;
    background: var(--page);
  }
  .canvas {
    position: relative;
    width: 1200px;
    height: 999px;
    font-family: "Raleway", sans-serif;
    font-variant-numeric: lining-nums;
    font-feature-settings: "lnum" 1;
    color: var(--ink-white);
  }
  .sign-panel {
    position: absolute;
    left: 236px;
    top: 44px;
    width: 729px;
    height: 873px;
    background: var(--sign-black);
  }
  .sign-trim {
    position: absolute;
    left: 236px;
    top: 917px;
    width: 729px;
    height: 37px;
    background: var(--trim-tan);
  }
  .brand-name {
    position: absolute;
    left: 236px;
    top: 150px;
    width: 729px;
    text-align: center;
    font-weight: 500;
    font-size: 46px;
    letter-spacing: 9px;
    line-height: 1;
    white-space: nowrap;
  }
  .headshot {
    position: absolute;
    left: 663px;
    top: 354px;
    width: 264px;
    height: 264px;
    border-radius: 50%;
    background: var(--ink-white);
    padding: 10px;
  }
  .headshot-fill {
    width: 100%;
    height: 100%;
    border-radius: 50%;
    background: radial-gradient(circle at 50% 35%, var(--photo-green) 0%, #8d9a7c 45%, var(--photo-grey) 100%);
  }
  .agent-name {
    position: absolute;
    left: 330px;
    top: 582px;
    font-weight: 500;
    font-size: 37px;
    letter-spacing: 1.5px;
    line-height: 1;
    white-space: nowrap;
  }
  .agent-phone {
    position: absolute;
    left: 328px;
    top: 645px;
    font-weight: 300;
    font-size: 92px;
    line-height: 1;
    white-space: nowrap;
  }
  .contact-item {
    position: absolute;
    top: 786px;
    height: 58px;
    display: flex;
    align-items: center;
    gap: 8px;
    font-weight: 500;
    font-size: 17px;
    white-space: nowrap;
  }
  .contact-email { left: 290px; }
  .contact-web { left: 664px; }
  .contact-icon { display: block; flex: none; }
</style>
</head>
<body>
<div class="canvas">
  <div class="sign-panel"></div>
  <div class="sign-trim"></div>

  <div class="brand-name">HOLLET HOMES</div>

  <div class="headshot">
    <div class="headshot-fill" role="img" aria-label="Agent headshot photograph"></div>
  </div>

  <div class="agent-name">MARCUS HOLLET</div>
  <div class="agent-phone">555.317.2096</div>

  <div class="contact-item contact-email">
    <svg class="contact-icon" width="72" height="54" viewBox="0 0 72 54" aria-hidden="true">
      <rect x="2" y="2" width="68" height="50" fill="none" stroke="#fff" stroke-width="3"/>
      <polyline points="2,2 36,30 70,2" fill="none" stroke="#fff" stroke-width="3"/>
      <line x1="2" y1="52" x2="28" y2="24" stroke="#fff" stroke-width="3"/>
      <line x1="70" y1="52" x2="44" y2="24" stroke="#fff" stroke-width="3"/>
      <text x="36" y="21" text-anchor="middle" font-family="Raleway, sans-serif" font-size="14" font-weight="500" fill="#fff">@</text>
    </svg>
    <span>Marcus@MHolletHomes.example</span>
  </div>

  <div class="contact-item contact-web">
    <svg class="contact-icon" width="64" height="64" viewBox="0 0 64 64" aria-hidden="true">
      <circle cx="31" cy="30" r="28" fill="none" stroke="#fff" stroke-width="3"/>
      <ellipse cx="31" cy="30" rx="12" ry="28" fill="none" stroke="#fff" stroke-width="3"/>
      <line x1="31" y1="2" x2="31" y2="58" stroke="#fff" stroke-width="3"/>
      <line x1="4" y1="21" x2="58" y2="21" stroke="#fff" stroke-width="3"/>
      <line x1="4" y1="39" x2="58" y2="39" stroke="#fff" stroke-width="3"/>
      <polygon points="38,36 38,62 44,56 49,64 53,62 48,54 56,53" fill="#fff" stroke="#000" stroke-width="2"/>
    </svg>
    <span>MHolletHomes.example</span>
  </div>
</div>
</body>
</html>
```